"Thank You" flyer design

We need a "thank you" flyer that will be sent out with all our products.
a6 size landscape,
We manufacture personalised shaped signs.
I've attached a rough idea of what we are after, but would like it to be improved upon with some artistic flare..

Side one - We would like the flyer to have a simple message - "thank you for shopping with us"

Side two - we would also like our logo and a union jack made in the UK badge and our address and contact details with our website www.lumkinprints.co.uk being the most prominent..

We are after a simple bold design what would be printed on a small a6 card that people might hopefully want to keep, so the end design needs to be pretty cool.

Industry/Entity Type

Shopping

Font styles to use
Serif
Sans Serif

```html
<!DOCTYPE html>
<html lang="en">
<head>
<meta charset="utf-8">
<title>Lumkin Prints – Thank You Flyer</title>
<link rel="stylesheet" href="https://fonts.googleapis.com/css2?family=Cinzel:wght@400;700&family=Tinos&display=swap">
<style>
  :root {
    --magenta: #e81af1;
    --ink: #1f1f1f;
    --paper: #ffffff;
    --edge: #000000;
  }
  * { box-sizing: border-box; margin: 0; padding: 0; }
  html, body { width: 1200px; height: 1000px; overflow: hidden; background: var(--paper); }
  body { position: relative; font-family: "Cinzel", Georgia, serif; color: var(--ink); }

  .flyer {
    position: absolute;
    width: 698px; height: 425px;
    border: 1px solid var(--edge);
    background: var(--paper);
    overflow: hidden;
  }
  .flyer--info { left: 294px; top: 49px; }
  .flyer--thanks { left: 300px; top: 502px; }

  .wave { position: absolute; left: 0; top: 0; width: 698px; height: 425px; }
  .wave path { fill: var(--magenta); }

  .brand-name {
    position: absolute;
    font-family: "Cinzel", Georgia, serif;
    font-weight: 700;
    color: var(--magenta);
    line-height: 1;
    text-align: center;
  }
  .flyer--info .brand-name { left: 126px; top: 150px; width: 330px; font-size: 60px; line-height: 1.05; }
  .flyer--thanks .brand-name { left: 5px; top: 110px; width: 210px; font-size: 36px; line-height: 1.1; }

  .visit { position: absolute; left: 428px; top: 130px; width: 260px; }
  .visit__lead { font-size: 19px; line-height: 24px; }
  .visit__url {
    display: inline-block;
    font-weight: 700; font-size: 18px; line-height: 24px;
    border-bottom: 2px solid var(--magenta);
    padding-bottom: 1px;
  }
  .visit__tagline { margin-top: 8px; font-size: 18px; line-height: 28px; }

  .contact {
    position: absolute; left: 497px; top: 372px;
    color: var(--paper);
    font-size: 19px; line-height: 21px;
  }
  .contact__number {
    display: flex; align-items: center; gap: 3px;
    font-family: "Tinos", "Times New Roman", serif;
    font-size: 20px; padding-left: 4px;
  }
  .contact__icon { width: 22px; height: 16px; }
  .contact__icon path { fill: var(--paper); }

  .divider {
    position: absolute; left: 224px; top: 63px;
    width: 3px; height: 180px; background: var(--magenta);
  }
  .thanks { position: absolute; left: 238px; top: 74px; }
  .thanks__message {
    font-size: 47px; font-weight: 400; line-height: 52px;
    letter-spacing: 1px; color: var(--ink);
  }
  .thanks__url { margin-top: 2px; font-weight: 700; font-size: 17px; }
</style>
</head>
<body>

<section class="flyer flyer--info">
  <svg class="wave" viewBox="0 0 698 425" aria-hidden="true">
    <path d="M0,277 C50,330 120,365 195,390 C120,373 50,350 0,330 Z"/>
    <path d="M430,383 C520,330 600,268 698,265 L698,279 C600,285 520,332 430,383 Z"/>
    <path d="M0,327 C120,388 300,412 430,385 C530,362 600,293 698,290 L698,425 L0,425 Z"/>
  </svg>
  <div class="brand-name">LUMKIN<br>PRINTS</div>
  <div class="visit">
    <p class="visit__lead">Please visit</p>
    <p class="visit__url">www.lumkinprints.co.uk</p>
    <p class="visit__tagline">For personalized<br>&nbsp;Shaped signs</p>
  </div>
  <div class="contact">
    <p>Call our team on</p>
    <p class="contact__number">
      <svg class="contact__icon" viewBox="0 0 22 16" aria-hidden="true"><path d="M2,5 C2,1 20,1 20,5 L20,7 L15,7 L15,5 L7,5 L7,7 L2,7 Z M5,8 L17,8 L20,15 L2,15 Z"/></svg>
      01632 960418
    </p>
  </div>
</section>

<section class="flyer flyer--thanks">
  <svg class="wave" viewBox="0 0 698 425" aria-hidden="true">
    <path d="M0,277 C50,330 120,365 195,390 C120,373 50,350 0,330 Z"/>
    <path d="M430,383 C520,330 600,268 698,265 L698,279 C600,285 520,332 430,383 Z"/>
    <path d="M0,327 C120,388 300,412 430,385 C530,362 600,293 698,290 L698,425 L0,425 Z"/>
  </svg>
  <div class="brand-name">LUMKIN<br>PRINTS</div>
  <div class="divider"></div>
  <div class="thanks">
    <h1 class="thanks__message">THANK YOU<br>FOR SHOPPING<br>WITH US!</h1>
    <p class="thanks__url">www.lumkinprints.co.uk</p>
  </div>
  <div class="contact">
    <p>Call our team on</p>
    <p class="contact__number">
      <svg class="contact__icon" viewBox="0 0 22 16" aria-hidden="true"><path d="M2,5 C2,1 20,1 20,5 L20,7 L15,7 L15,5 L7,5 L7,7 L2,7 Z M5,8 L17,8 L20,15 L2,15 Z"/></svg>
      01632 960418
    </p>
  </div>
</section>

</body>
</html>
```